Postcard: Open Sky Circle

Text for front: HOW TO CHANGE THE WORLD IN ONE [note: the word "one" should be underlined] STEPHint: It's up to you...[Note: add arrow or something to indicate "turn over"]Text for back: You're going to spend your entire life with someone you can never get away from. (Guess who?) Wouldn't you rather that person #OpenSkyCircle than judgmental or critical? BE the change you want to see! Visit www.OpenSkyCircle-hub.example for daily Dawn Pebbles and community. PLEASE JOIN US![Note: add logo to left half of back side]Font preference for text: Josefin sans

Target Market(s)

People who would be attracted to Corvane church - teravian perennist message. It's spiritual without being overtly religious, so the target market is probably early 30s and up but ideally won't turn off Millennials (folks under 30). It should attract attention of people who are open-minded and committed to progressive social change, tired of an atmosphere of hate-mongering and divisiveness.

Requirements
Nice to have
• It would be nice to convey a sense of challenge - there is an idea of "dawn pebbles" so something related to fire/sparks is appropriate. This is meant to evoke a deeper, divine love more than a sense of romantic love. This love is more fierce than fluffy! Yet it calls us to be our best selves.
Should not have
• Please avoid excessive pink - just the logo is enough, as this design needs to appeal to men as well as women.

```html
<!DOCTYPE html>
<html lang="en">
<head>
<meta charset="utf-8">
<title>Open Sky Circle Postcard</title>
<link rel="stylesheet" href="https://fonts.googleapis.com/css2?family=Bebas+Neue&family=Josefin+Sans:wght@300;400&family=Roboto+Slab:wght@500&display=swap">
<style>
  :root {
    --pink: #ee6b9b;
    --hot-pink: #e8416f;
    --ink: #2d2d2f;
    --white: #ffffff;
    --steel-light: #e3e4e6;
    --steel-mid: #c8c9cc;
    --steel-dark: #b3b4b7;
  }
  * { margin: 0; padding: 0; box-sizing: border-box; }
  html, body {
    width: 1200px; height: 1200px; overflow: hidden;
    background: var(--white);
  }
  .canvas { position: relative; width: 1200px; height: 1200px; }

  .card {
    position: absolute; top: 205px;
    height: 914px; overflow: hidden;
    transform: scale(0.8); transform-origin: top left;
    background: linear-gradient(135deg, var(--steel-mid) 0%, var(--steel-light) 45%, var(--steel-dark) 100%);
  }
  .card--front { left: 80px; width: 622px; }
  .card--back { left: 622px; width: 626px; }

  .card__bands { position: absolute; inset: 0; width: 100%; height: 100%; }

  /* Front */
  .frame-outer {
    position: absolute; left: 24px; top: 232px; width: 574px; height: 410px;
    border: 7px solid var(--white); transform: rotate(2deg);
  }
  .frame-inner {
    position: absolute; left: 40px; top: 254px; width: 543px; height: 365px;
    border: 6px solid var(--hot-pink);
  }
  .headline {
    position: absolute; left: 40px; top: 284px; width: 543px;
    font-family: "Bebas Neue", sans-serif;
    font-size: 112px; line-height: 92px; letter-spacing: -4px;
    color: var(--ink); text-align: center;
  }
  .headline__accent { color: var(--hot-pink); }
  .headline__emphasis { text-decoration: underline; text-decoration-thickness: 5px; text-underline-offset: 6px; }

  .turn-ribbon { position: absolute; left: 160px; top: 520px; width: 390px; height: 110px; }
  .turn-ribbon__text {
    position: absolute; left: 192px; top: 588px;
    font-family: "Roboto Slab", serif; font-size: 17px; letter-spacing: 0.3px;
    color: var(--white); transform: rotate(-3deg); transform-origin: left center;
    white-space: nowrap;
  }

  .hint {
    position: absolute; left: 43px; top: 832px;
    font-family: "Josefin Sans", sans-serif; font-weight: 400;
    font-size: 42px; color: var(--white);
  }

  /* Back */
  .brand {
    position: absolute; left: 0; top: 110px; width: 100%;
    display: flex; align-items: center; justify-content: center; gap: 12px;
    font-family: "Josefin Sans", sans-serif; font-weight: 400;
    font-size: 34px; color: var(--hot-pink);
  }
  .brand__dot { width: 18px; height: 18px; border-radius: 50%; background: var(--hot-pink); }

  .message {
    position: absolute; left: 68px; top: 252px; width: 540px;
    font-family: "Josefin Sans", sans-serif; font-weight: 300;
    font-size: 30px; line-height: 41px; color: var(--ink);
  }
  .message__question {
    display: block; color: var(--hot-pink);
    font-size: 52px; line-height: 60px; margin: 2px 0 4px;
  }
  .message__url {
    display: block; font-weight: 400;
    font-size: 33px; line-height: 44px; margin-top: 6px; white-space: nowrap;
  }
  .message__url-name { color: var(--hot-pink); }

  .join {
    position: absolute; left: 26px; top: 800px;
    font-family: "Bebas Neue", sans-serif;
    font-size: 100px; line-height: 1; letter-spacing: -3px;
    color: var(--ink);
  }
  .join__accent { color: var(--white); }
</style>
</head>
<body>
<main class="canvas">

  <section class="card card--front" aria-label="Postcard front">
    <svg class="card__bands" viewBox="0 0 622 914" preserveAspectRatio="none" aria-hidden="true">
      <polygon points="0,0 622,0 622,244 0,24" fill="var(--pink)"/>
      <polygon points="0,624 622,804 622,914 0,914" fill="var(--pink)"/>
    </svg>
    <div class="frame-outer"></div>
    <div class="frame-inner"></div>
    <h1 class="headline">
      HOW TO CHANGE<br>
      THE <span class="headline__accent">WORLD</span><br>
      IN <span class="headline__emphasis">ONE</span> STEP
    </h1>
    <svg class="turn-ribbon" viewBox="0 0 390 110" aria-hidden="true">
      <polygon points="5,58 345,38 352,76 10,96" fill="var(--hot-pink)"/>
      <path d="M330,40 C360,20 385,0 372,40 C365,62 352,72 345,76 Z" fill="#c8246a"/>
    </svg>
    <p class="turn-ribbon__text">SEE BACK FOR MORE DETAILS!</p>
    <p class="hint">Hint: It's up to you...</p>
  </section>

  <section class="card card--back" aria-label="Postcard back">
    <svg class="card__bands" viewBox="0 0 626 914" preserveAspectRatio="none" aria-hidden="true">
      <polygon points="0,629 626,824 626,914 0,914" fill="var(--pink)"/>
    </svg>
    <div class="brand"><span class="brand__dot"></span>Open Sky Circle</div>
    <p class="message">
      You're going to spend your entire life with someone you can never get away from.
      <span class="message__question">(GUESS WHO?)</span>
      Wouldn't you rather that person #OpenSkyCircle than judgmental or critical? BE the change you want to see! Visit:
      <span class="message__url">www.<span class="message__url-name">OpenSkyCircle</span>-hub.example</span>
      for daily Dawn Pebbles and community.
    </p>
    <p class="join">PLEASE <span class="join__accent">JOIN</span> US!</p>
  </section>

</main>
</body>
</html>
```